A label for my commercially sold local honey. This is a LABEL not a logo

3 inches high
2 inches wide

Target Market(s)

Customers who like "local" honey

Logo Text

Wildflower Honey -- 100% Pure & Unfiltered -- Florida

Logo styles of interest
Wordmark Logo
Requirements
Must have
• Wildflower Honey -- 100% Pure & Unfiltered -- Florida

Florida should be dominant

3 inches high / 2 inches wide

```html
<!DOCTYPE html>
<html lang="en">
<head>
<meta charset="utf-8">
<title>Wildflower Honey Label</title>
<link href="https://fonts.googleapis.com/css2?family=Roboto+Slab:wght@800&family=Roboto+Condensed:wght@700&family=Montserrat:wght@700&display=swap" rel="stylesheet">
<style>
  :root {
    --backdrop: #d47a26;
    --label-black: #1b1b1b;
    --lattice-dark: #232323;
    --lattice-mid: #2e2b26;
    --gold: #f5b21a;
    --gold-light: #ffd35a;
    --gold-deep: #e39a0c;
    --white: #ffffff;
    --ink: #1b1b1b;
  }
  * { margin: 0; padding: 0; box-sizing: border-box; }
  html, body {
    width: 1200px;
    height: 871px;
    overflow: hidden;
  }
  body {
    background: var(--backdrop);
    position: relative;
  }
  .label {
    position: absolute;
    left: 340px;
    top: 45px;
    width: 520px;
    height: 780px;
    background: var(--label-black);
    overflow: hidden;
  }
  .gold-rule {
    position: absolute;
    left: 0;
    width: 100%;
    background: linear-gradient(90deg, var(--gold-deep), var(--gold-light) 50%, var(--gold-deep));
  }
  .gold-rule--top { top: 16px; height: 5px; }
  .gold-rule--upper-thin { top: 192px; height: 4px; }
  .gold-rule--upper-thick { top: 201px; height: 10px; }
  .gold-rule--lower-a { top: 704px; height: 5px; }
  .gold-rule--lower-b { top: 730px; height: 5px; }

  .brand-seal {
    position: absolute;
    left: 50%;
    top: 28px;
    width: 170px;
    height: 170px;
    margin-left: -85px;
    border-radius: 50%;
    background: var(--white);
    border: 5px solid var(--gold);
    display: flex;
    align-items: center;
    justify-content: center;
    text-align: center;
    z-index: 2;
  }
  .brand-name {
    font-family: "Roboto Condensed", sans-serif;
    font-weight: 700;
    font-size: 26px;
    line-height: 1.05;
    color: var(--ink);
    letter-spacing: 1px;
    text-transform: uppercase;
  }

  .lattice-field {
    position: absolute;
    left: 0;
    top: 211px;
    width: 100%;
    height: 324px;
    background: radial-gradient(ellipse at 50% 55%, var(--lattice-mid), var(--lattice-dark) 75%);
  }
  .product-title {
    position: absolute;
    left: 0;
    width: 100%;
    text-align: center;
    font-family: "Roboto Slab", serif;
    font-weight: 800;
    color: var(--white);
    text-transform: uppercase;
    white-space: nowrap;
  }
  .product-title__variety {
    position: absolute;
    left: 0;
    top: 272px;
    width: 100%;
    font-size: 60px;
    line-height: 80px;
    transform: scaleY(1.35);
  }
  .product-title__name {
    position: absolute;
    left: 0;
    top: 360px;
    width: 100%;
    font-size: 118px;
    line-height: 150px;
    transform: scaleY(1.4);
  }

  .claim-band {
    position: absolute;
    left: 0;
    top: 537px;
    width: 100%;
    height: 54px;
    background: linear-gradient(90deg, var(--gold-deep), var(--gold-light) 50%, var(--gold-deep));
    display: flex;
    align-items: center;
    justify-content: center;
  }
  .claim-text {
    font-family: "Roboto Condensed", sans-serif;
    font-weight: 700;
    font-size: 33px;
    color: var(--ink);
    text-transform: uppercase;
  }

  .origin {
    position: absolute;
    left: 0;
    top: 612px;
    width: 100%;
    text-align: center;
    font-family: "Montserrat", sans-serif;
    font-weight: 700;
    font-size: 54px;
    line-height: 70px;
    letter-spacing: 3px;
    color: var(--white);
    text-transform: uppercase;
  }

  .net-weight {
    position: absolute;
    left: 50%;
    top: 696px;
    width: 46px;
    height: 46px;
    margin-left: -23px;
    border-radius: 50%;
    background: var(--gold);
    display: flex;
    align-items: center;
    justify-content: center;
    font-family: "Roboto Condensed", sans-serif;
    font-weight: 700;
    font-size: 17px;
    color: var(--ink);
    z-index: 2;
  }
</style>
</head>
<body>
  <main class="label">
    <div class="gold-rule gold-rule--top"></div>

    <div class="brand-seal">
      <span class="brand-name">Bramble<br>Hive</span>
    </div>

    <div class="gold-rule gold-rule--upper-thin"></div>
    <div class="gold-rule gold-rule--upper-thick"></div>

    <div class="lattice-field" role="img" aria-label="Dark honeycomb lattice pattern with small gold dots"></div>

    <h1 class="product-title">
      <span class="product-title__variety">Wildflower</span>
      <span class="product-title__name">Honey</span>
    </h1>

    <div class="claim-band">
      <p class="claim-text">100% Pure &amp; Unfiltered</p>
    </div>

    <p class="origin">Florida</p>

    <div class="gold-rule gold-rule--lower-a"></div>
    <div class="gold-rule gold-rule--lower-b"></div>
    <div class="net-weight">12oz</div>
  </main>
</body>
</html>
```